Business Card Design Project

I want a new business card for all 5 of my companies. Card needs to be double sided with my name and details on one side and all 5 logos on the other side.

Industry/Entity Type

Business

```html
<!DOCTYPE html>
<html lang="en">
<head>
<meta charset="utf-8">
<title>Verano Group – Business Card</title>
<link rel="stylesheet" href="https://fonts.googleapis.com/css2?family=Old+Standard+TT:wght@400;700&family=Archivo:wght@400;600;800&display=swap">
<style>
  :root {
    --stage: #e9e9e9;
    --card: #ffffff;
    --card-soft: #f3f3f3;
    --ink: #111111;
    --ink-soft: #444444;
    --slate: #3f4650;
    --rule: #c9c9c9;
    --lime: #cdf55a;
    --green: #7df05a;
    --green-deep: #4ef021;
    --aqua: #b4f7f7;
    --sky: #8fd6f2;
    --mark-tone: #f2b63a;
  }
  * { box-sizing: border-box; margin: 0; padding: 0; }
  html, body { width: 1200px; height: 1189px; overflow: hidden; }
  body { background: var(--stage); position: relative; font-family: "Archivo", sans-serif; }

  .card { position: absolute; width: 692px; height: 392px; overflow: hidden; box-shadow: 0 2px 8px rgba(0,0,0,.18); }

  /* Front: personal details */
  .card-front { left: 180px; top: 178px; background: linear-gradient(135deg, var(--card) 0%, var(--card-soft) 100%); }
  .divider { position: absolute; left: 338px; width: 2px; background: var(--rule); }
  .divider-top { top: 14px; height: 158px; }
  .divider-bottom { top: 220px; height: 158px; }
  .feature-art { position: absolute; left: 384px; top: 0; width: 308px; height: 392px;
    border-radius: 160px 0 0 160px;
    background: radial-gradient(circle at 70% 30%, var(--green-deep) 0%, var(--green) 45%, var(--lime) 100%); }

  .name-bar { position: absolute; left: 0; top: 262px; width: 252px; height: 29px; background: var(--ink);
    border-radius: 0 15px 15px 0; display: flex; align-items: center; justify-content: center; padding-right: 20px; }
  .owner-name { font-family: "Old Standard TT", serif; color: #fff; font-size: 19px; letter-spacing: .5px; }

  .contact-list { position: absolute; left: 60px; top: 302px; list-style: none; }
  .contact-list li { display: flex; align-items: center; height: 28px; font-family: "Old Standard TT", serif; font-size: 12px; color: var(--ink-soft); }
  .contact-list svg { width: 22px; height: 22px; margin-right: 13px; }

  /* Back: group companies */
  .card-back { left: 324px; top: 606px; background: var(--card); }
  .band { position: absolute; inset: 0; }

  .mark-square { position: absolute; background: var(--mark-tone); }
  .square-mend { left: 96px; top: 30px; width: 56px; height: 56px; }
  .square-rigg { left: 238px; top: 74px; width: 84px; height: 84px; }
  .square-fence { left: 292px; top: 304px; width: 40px; height: 40px; }

  .mark-name { position: absolute; font-weight: 600; color: var(--slate); font-size: 17px; letter-spacing: -.3px; white-space: nowrap; }
  .mark-mend { left: 80px; top: 96px; }
  .mark-rigg { left: 228px; top: 170px; font-size: 21px; }
  .mark-fence { left: 346px; top: 306px; font-size: 30px; line-height: 36px; }

  .brand { position: absolute; }
  .brand-dot { width: 30px; height: 30px; border-radius: 50%; margin-bottom: 8px; }
  .brand-name { font-size: 26px; line-height: 28px; font-weight: 600; letter-spacing: -.8px; color: var(--slate); }
  .brand-structural { left: 470px; top: 22px; }
  .brand-structural .brand-dot { background: var(--green); }
  .brand-caulking { left: 18px; top: 257px; }
  .brand-caulking .brand-dot { background: var(--sky); }
</style>
</head>
<body>

<section class="card card-front" aria-label="Card front">
  <div class="divider divider-top"></div>
  <div class="divider divider-bottom"></div>
  <div class="feature-art" role="img" aria-label="Large green and lime decorative shape"></div>

  <div class="name-bar"><span class="owner-name">Owner Name</span></div>

  <ul class="contact-list">
    <li>
      <svg viewBox="0 0 24 24" aria-hidden="true"><path fill="#9a9a9a" d="M6.6 10.8a15 15 0 0 0 6.6 6.6l2.2-2.2c.3-.3.7-.4 1-.2 1.1.4 2.3.6 3.6.6.6 0 1 .4 1 1V20c0 .6-.4 1-1 1A17 17 0 0 1 3 4c0-.6.4-1 1-1h3.5c.6 0 1 .4 1 1 0 1.3.2 2.5.6 3.6.1.3 0 .7-.2 1z"/></svg>
      08 5550 1234
    </li>
    <li>
      <svg viewBox="0 0 24 24" aria-hidden="true"><rect x="2" y="5" width="20" height="14" rx="1" fill="#9a9a9a"/><path d="M2 6l10 7 10-7" fill="none" stroke="#fff" stroke-width="1.5"/></svg>
      email@veranogroup.com.au
    </li>
    <li>
      <svg viewBox="0 0 24 24" aria-hidden="true"><g fill="none" stroke="#9a9a9a" stroke-width="1.6"><circle cx="12" cy="12" r="9"/><ellipse cx="12" cy="12" rx="4" ry="9"/><path d="M3 12h18M5 7h14M5 17h14"/></g></svg>
      www.veranogroup.com.au
    </li>
  </ul>
</section>

<section class="card card-back" aria-label="Card back">
  <svg class="band" viewBox="0 0 692 392" preserveAspectRatio="none" aria-hidden="true">
    <polygon points="0,0 692,0 692,256 0,137" fill="var(--aqua)"/>
  </svg>

  <div class="mark-square square-mend" role="img" aria-label="Company mark of Mendworks"></div>
  <span class="mark-name mark-mend">Mendworks</span>

  <div class="mark-square square-rigg" role="img" aria-label="Company mark of Riggworks"></div>
  <span class="mark-name mark-rigg">Riggworks</span>

  <div class="brand brand-structural">
    <div class="brand-dot"></div>
    <div class="brand-name">Verano<br>Structural</div>
  </div>

  <div class="brand brand-caulking">
    <div class="brand-dot"></div>
    <div class="brand-name">Sealwell<br>Caulking</div>
  </div>

  <div class="mark-square square-fence" role="img" aria-label="Company mark of Fenceline Hire"></div>
  <span class="mark-name mark-fence">Fenceline Hire</span>
</section>

</body>
</html>
```